NEW Household Invention Needs a Package Design!

We need a 'retail' package design for a new product invented for the household kitchen market. Brimloft has developed a reusable food storage system that can be tailored to an individual's needs and have a sustainable impact on their ability to make good dietary decisions, while helping save the planet. We would like to see designs that use the brand's branding guidelines and logo. The final design should communicate the key features of the product (patented customizable modular system, fill lines, collapsible functionality and sustainable materials), as well as, all other notable aspects (Microwave/Dishwasher Safe, Leakproof, 100% BPA Free, Donates 1% of purchase price, etc.). It's important that the benefits of the product are well highlighted (More variety to better balance nutrition, More easily stored in bag, kitchen cabinet or drawer and Ends waste)
Updates

Hi All, we are looking for a package design for retail, something that will be on a shelf in our product category.

Target Market(s)

Health conscious men and women who have a passion for nutrition & social responsibility, operate a lifestyle on-the-go and monitor their spending by preparing meals at home.

Industry/Entity Type

Food Tech, Consumer Products, Health & Wellness

Font styles to use
Other font styles liked:
• See Brand Guidelines

Requirements
Must have
• Follow brand guidelines: https://guidelines.quorvadesign.example/brimloft/guidelines/

```html
<!DOCTYPE html>
<html lang="en">
<head>
<meta charset="utf-8">
<title>Brimloft – Reusable Food Storage System carton dieline</title>
<link rel="stylesheet" href="https://fonts.googleapis.com/css2?family=Montserrat:wght@400;500;600;700&family=Caveat+Brush&display=swap">
<style>
  :root {
    --kraft: #d3b089;
    --kraft-dark: #c9a47a;
    --ink: #2a2521;
    --plum: #8b2a6f;
    --page: #ffffff;
    --dot-green: #a9d39a;
    --dot-pink: #d8a7b1;
    --dot-blue: #6fc3e6;
  }
  * { box-sizing: border-box; margin: 0; padding: 0; }
  html, body { width: 1200px; height: 3047px; overflow: hidden; background: var(--page); }
  body { position: relative; font-family: "Montserrat", sans-serif; color: var(--ink); }

  .panel {
    position: absolute;
    background: linear-gradient(135deg, var(--kraft) 0%, var(--kraft-dark) 100%);
    overflow: hidden;
  }
  .flap-top { left: 288px; top: 1156px; width: 312px; height: 248px; }
  .band { left: 40px; top: 1404px; width: 1120px; height: 238px; }
  .flap-bottom { left: 288px; top: 1642px; width: 312px; height: 248px; }

  .face { position: absolute; top: 0; height: 238px; }
  .face-features { left: 0; width: 248px; }
  .face-front { left: 248px; width: 312px; }
  .face-side { left: 560px; width: 248px; }
  .face-back { left: 808px; width: 312px; }

  .brand { position: absolute; text-align: center; }
  .brand-name { font-weight: 600; letter-spacing: -0.5px; line-height: 1; display: block; }
  .brand-sub {
    display: flex; align-items: center; gap: 5px; justify-content: center;
    font-size: 6px; font-weight: 600; letter-spacing: 0.2px; margin-top: 3px; white-space: nowrap;
  }
  .brand-sub::before, .brand-sub::after { content: ""; width: 14px; height: 1px; background: var(--ink); }

  .tagline {
    position: absolute; font-family: "Caveat Brush", cursive; line-height: 0.95; text-align: center;
  }

  .flap-top .tagline { left: 0; right: 0; top: 20px; font-size: 22px; transform: rotate(180deg); }
  .flap-top .brand { left: 0; right: 0; top: 118px; }
  .flap-top .brand-name { font-size: 28px; }

  .feature { position: absolute; width: 110px; text-align: center; font-size: 8px; font-weight: 600; line-height: 1.2; }
  .feature svg { display: block; margin: 0 auto 6px; }

  .face-front .brand { left: 10px; top: 16px; width: 130px; }
  .face-front .brand-name { font-size: 26px; }
  .face-front .tagline { right: 14px; top: 18px; font-size: 18px; }
  .hero-art {
    position: absolute; left: 14px; top: 62px; width: 240px; height: 92px; border-radius: 6px;
    background: linear-gradient(90deg, #d96a63 0%, #9fcbe6 30%, #a9d2ea 65%, #6e8f3c 85%, #e86d55 100%);
  }
  .helping { position: absolute; left: 12px; top: 158px; font-size: 8px; font-weight: 700; color: var(--plum); }
  .plum-band { position: absolute; left: 0; right: 0; top: 172px; height: 36px; background: var(--plum); }
  .care-icon { position: absolute; top: 7px; width: 20px; height: 20px; border: 1.2px solid #e9c9dd; border-radius: 2px; }
  .bpa-badge {
    position: absolute; right: 8px; top: 176px; width: 30px; height: 30px; border-radius: 50%;
    background: var(--kraft); border: 1.5px solid var(--plum);
  }

  .face-side .tagline { left: 0; right: 0; top: 22px; font-size: 25px; }
  .face-side .brand { left: 0; right: 0; top: 92px; }
  .face-side .brand-name { font-size: 34px; }
  .colour { position: absolute; left: 12px; top: 198px; font-size: 6px; font-weight: 600; }
  .colour-dots { display: flex; gap: 3px; margin-top: 2px; }
  .colour-dots span { width: 9px; height: 9px; border-radius: 50%; border: 1.5px solid; }
  .capacity { position: absolute; right: 14px; top: 200px; font-size: 6.5px; font-weight: 600; text-align: right; line-height: 1.3; }

  .face-back .brand { left: 0; right: 0; top: 16px; }
  .face-back .brand-name { font-size: 26px; }
  .intro { position: absolute; left: 14px; right: 14px; top: 56px; font-size: 4.6px; line-height: 1.45; }
  .benefits { position: absolute; left: 14px; top: 90px; width: 130px; list-style: none; }
  .benefits li { display: flex; gap: 4px; font-size: 4.6px; line-height: 1.35; margin-bottom: 9px; }
  .benefits svg { flex: none; }
  .contact { position: absolute; right: 14px; top: 92px; width: 110px; text-align: right; font-size: 4.6px; line-height: 1.5; }
  .contact .follow { font-weight: 700; font-size: 5.5px; margin-bottom: 4px; }
  .contact .maker span { color: var(--plum); font-weight: 600; }
</style>
</head>
<body>

  <section class="panel flap-top">
    <p class="tagline">For People<br>&amp; Planet</p>
    <div class="brand">
      <span class="brand-name">Brimloft</span>
      <span class="brand-sub">REUSABLE FOOD STORAGE SYSTEM</span>
    </div>
  </section>

  <section class="panel band">

    <div class="face face-features">
      <div class="feature" style="left:12px; top:26px;">
        <svg width="40" height="40" viewBox="0 0 40 40"><circle cx="20" cy="20" r="18" fill="none" stroke="#2a2521" stroke-width="1.2" stroke-dasharray="1.5 1.5"/><circle cx="20" cy="20" r="14" fill="none" stroke="#2a2521" stroke-width="1.4"/><path d="M20 10c-3 5-5 7-5 10a5 5 0 0 0 10 0c0-3-2-5-5-10z" fill="#8b2a6f"/></svg>
        Leakproof
      </div>
      <div class="feature" style="left:126px; top:26px;">
        <svg width="40" height="40" viewBox="0 0 40 40"><circle cx="20" cy="20" r="18" fill="none" stroke="#2a2521" stroke-width="1.2" stroke-dasharray="1.5 1.5"/><circle cx="20" cy="20" r="14" fill="#8b2a6f"/><path d="M13 26c0-8 6-13 14-13-1 8-6 13-14 13zM13 26l9-8" fill="#d3b089" stroke="#8b2a6f" stroke-width="1"/></svg>
        100% BPA Free
      </div>
      <div class="feature" style="left:12px; top:122px;">
        <svg width="40" height="40" viewBox="0 0 40 40"><circle cx="20" cy="20" r="18" fill="none" stroke="#2a2521" stroke-width="1.2" stroke-dasharray="1.5 1.5"/><circle cx="20" cy="20" r="14" fill="#8b2a6f"/><rect x="11" y="14" width="18" height="12" rx="1.5" fill="none" stroke="#d3b089" stroke-width="1.4"/><rect x="13" y="16" width="10" height="8" fill="#d3b089"/></svg>
        Microwave/<br>Dishwasher Safe
      </div>
      <div class="feature" style="left:126px; top:122px;">
        <svg width="40" height="40" viewBox="0 0 40 40"><circle cx="20" cy="20" r="18" fill="none" stroke="#2a2521" stroke-width="1.2" stroke-dasharray="1.5 1.5"/><circle cx="20" cy="20" r="14" fill="#8b2a6f"/><text x="20" y="26" text-anchor="middle" font-family="Montserrat, sans-serif" font-weight="700" font-size="17" fill="#d3b089">$</text></svg>
        Donates 1%<br>of purchase price
      </div>
    </div>

    <div class="face face-front">
      <div class="brand">
        <span class="brand-name">Brimloft</span>
        <span class="brand-sub">REUSABLE FOOD STORAGE SYSTEM</span>
      </div>
      <p class="tagline">For People<br>&amp; Planet</p>
      <div class="hero-art" role="img" aria-label="Illustration of blue collapsible food storage containers surrounded by watermelon, avocado, greens and fresh produce"></div>
      <p class="helping">Helping save the planet !</p>
      <div class="plum-band">
        <span class="care-icon" style="left:10px;"></span>
        <span class="care-icon" style="left:36px;"></span>
        <span class="care-icon" style="left:62px;"></span>
        <svg style="position:absolute; left:92px; top:8px;" width="40" height="18" viewBox="0 0 40 18"><path d="M9 2l6 10H3z M29 2l6 10H23z" fill="none" stroke="#e9c9dd" stroke-width="1.2"/></svg>
      </div>
      <div class="bpa-badge" role="img" aria-label="Certification badge"></div>
    </div>

    <div class="face face-side">
      <p class="tagline">For People<br>&amp; Planet</p>
      <div class="brand">
        <span class="brand-name">Brimloft</span>
        <span class="brand-sub">REUSABLE FOOD STORAGE SYSTEM</span>
      </div>
      <div class="colour">COLOUR
        <div class="colour-dots">
          <span style="border-color:var(--dot-green)"></span>
          <span style="border-color:var(--dot-pink)"></span>
          <span style="border-color:var(--dot-blue)"></span>
        </div>
      </div>
      <p class="capacity">5.5 CUP CAPACITY<br>(1000 ML)</p>
    </div>

    <div class="face face-back">
      <div class="brand">
        <span class="brand-name">Brimloft</span>
        <span class="brand-sub">REUSABLE FOOD STORAGE SYSTEM</span>
      </div>
      <p class="intro">Every Brimloft set is built to stack, fold and travel, so fresh meals stay simple from prep day to lunch break.</p>
      <ul class="benefits">
        <li><svg width="6" height="6" viewBox="0 0 6 6"><rect x="0.4" y="0.4" width="5.2" height="5.2" fill="none" stroke="#8b2a6f" stroke-width="0.7"/><path d="M1.3 3l1.2 1.2 2.2-2.4" fill="none" stroke="#8b2a6f" stroke-width="0.7"/></svg>A four-point locking lid with silicone seal keeps food airtight and leakproof</li>
        <li><svg width="6" height="6" viewBox="0 0 6 6"><rect x="0.4" y="0.4" width="5.2" height="5.2" fill="none" stroke="#8b2a6f" stroke-width="0.7"/><path d="M1.3 3l1.2 1.2 2.2-2.4" fill="none" stroke="#8b2a6f" stroke-width="0.7"/></svg>Made of sturdy, high-quality, BPA-free plastic</li>
        <li><svg width="6" height="6" viewBox="0 0 6 6"><rect x="0.4" y="0.4" width="5.2" height="5.2" fill="none" stroke="#8b2a6f" stroke-width="0.7"/><path d="M1.3 3l1.2 1.2 2.2-2.4" fill="none" stroke="#8b2a6f" stroke-width="0.7"/></svg>Clear design for quick recognition of contents</li>
        <li><svg width="6" height="6" viewBox="0 0 6 6"><rect x="0.4" y="0.4" width="5.2" height="5.2" fill="none" stroke="#8b2a6f" stroke-width="0.7"/><path d="M1.3 3l1.2 1.2 2.2-2.4" fill="none" stroke="#8b2a6f" stroke-width="0.7"/></svg>Ideal for fridge, freezer or pantry, and easy to carry to school or work</li>
      </ul>
      <div class="contact">
        <p class="follow">Follow us on</p>
        <p class="maker">Manufactured by: <span>Company Name</span></p>
        <p>Designed for daily use and built to last for many seasons of meals</p>
        <p>+1 555 014 2290</p>
        <p>hello@brimloft.example</p>
        <p>www.brimloft.example</p>
      </div>
    </div>

  </section>

  <section class="panel flap-bottom"></section>

</body>
</html>
```